VEK.PRO- Daniel Whitcombe Fitness- needs a clever business card using the logo, name, info, contact

I need a business card designed for my Online Personal Training company called VEK.PRO, abbreviation for Daniel Whitcombe Fitness. My company focuses on coaching in personal health and personal growth to unleash your greatest potential. I would like to see designs that use my color scheme of a redish-orange (C:0,M:84,Y:100,K:0), grey, white, black, and my company font is OSWALD. The final design should communicate some aspects of design, health, motivation, growth, in some way. The logo is very important to the company and can be displayed in any of the colors previously mentioned. Must include the company name, my website: www.vek.example , my email: dan@vek.example

Target Market(s)

Personal health, fitness, general public, those who lack knowledge, awareness, and confidence in personal health

Industry/Entity Type

Personal Trainer

Font styles to use
Other font styles liked:
• OSWALD. (Bold, Regular, Light)

Colors
f37122
ffffff
9d9d9d
000000

Requirements
Must have
• Must include the logo, company name, my website: www.vek.example , my email: dan@vek.example
Nice to have
• Variations of the colors scheme of a redish-orange (C:0,M:84,Y:100,K:0), grey, white, black. Logo, card, or text can be in any of these colors.
• Possible quote like "Take control of your personal health to unleash your greatest potential" or "Unleashing your greatness first begins with fitness of the body and mind"

```html
<!DOCTYPE html>
<html lang="en">
<head>
<meta charset="utf-8">
<title>VEK.PRO Business Card</title>
<link rel="stylesheet" href="https://fonts.googleapis.com/css2?family=Oswald:wght@300;400;700&family=Open+Sans:wght@400;600;700&display=swap">
<style>
  :root {
    --brand-red: #d32a1c;
    --ink: #1e1e1e;
    --ink-soft: #3a3a3a;
    --card: #f4f3f1;
    --backdrop: #dcdad6;
    --white: #ffffff;
  }
  html, body {
    margin: 0;
    width: 1200px;
    height: 969px;
    overflow: hidden;
    background: var(--backdrop);
  }
  .business-card {
    position: absolute;
    left: 165px;
    top: 247px;
    width: 870px;
    height: 493px;
    background: var(--card);
    border-radius: 26px;
    overflow: hidden;
    box-shadow: 0 10px 30px rgba(0,0,0,0.12);
  }
  .card-info {
    position: absolute;
    left: 37px;
    top: 34px;
    width: 520px;
    font-family: "Open Sans", Arial, sans-serif;
    color: var(--ink-soft);
  }
  .company-name {
    margin: 0;
    font-family: "Oswald", "Arial Narrow", sans-serif;
    font-weight: 700;
    font-size: 78px;
    line-height: 1;
    color: var(--ink);
    letter-spacing: 0.5px;
  }
  .company-fullname {
    margin: 6px 0 0;
    font-family: "Oswald", "Arial Narrow", sans-serif;
    font-weight: 400;
    font-size: 22px;
    line-height: 1.1;
    text-transform: uppercase;
    color: var(--ink-soft);
  }
  .trainer-name {
    margin: 52px 0 0;
    font-family: "Oswald", "Arial Narrow", sans-serif;
    font-weight: 400;
    font-size: 27px;
    line-height: 1.1;
    text-transform: uppercase;
    color: var(--brand-red);
  }
  .trainer-role {
    margin: 2px 0 0;
    font-size: 19px;
    font-weight: 600;
    color: var(--ink-soft);
  }
  .contact-list {
    list-style: none;
    margin: 26px 0 0;
    padding: 0;
    font-size: 19px;
    line-height: 27px;
  }
  .contact-list li {
    display: flex;
    align-items: center;
    gap: 12px;
  }
  .contact-icon { width: 15px; height: 15px; flex: none; }
  .service-title {
    margin: 28px 0 0;
    font-size: 19px;
    font-weight: 700;
    color: var(--brand-red);
  }
  .tagline {
    margin: 14px 0 0;
    font-size: 19px;
    line-height: 29px;
    color: var(--ink-soft);
  }
  .brand-panel {
    position: absolute;
    left: 580px;
    top: 0;
    width: 290px;
    height: 100%;
    background: var(--brand-red);
    display: flex;
    align-items: center;
    justify-content: center;
    gap: 14px;
  }
  .brand-dot {
    width: 22px;
    height: 22px;
    border-radius: 50%;
    background: var(--white);
  }
  .brand-wordmark {
    font-family: "Oswald", "Arial Narrow", sans-serif;
    font-weight: 700;
    font-size: 52px;
    color: var(--white);
    letter-spacing: 1px;
  }
</style>
</head>
<body>
  <div class="business-card">
    <div class="card-info">
      <h1 class="company-name">VEK.PRO</h1>
      <p class="company-fullname">Daniel Whitcombe Fitness</p>
      <p class="trainer-name">Daniel Whitcombe</p>
      <p class="trainer-role">Personal Trainer</p>
      <ul class="contact-list">
        <li>
          <svg class="contact-icon" viewBox="0 0 16 16" aria-hidden="true">
            <rect x="1" y="3" width="14" height="10" rx="1.5" fill="var(--brand-red)"/>
            <path d="M1.5 4 L8 9 L14.5 4" fill="none" stroke="var(--card)" stroke-width="1.4"/>
          </svg>
          dan@vek.example
        </li>
        <li>
          <svg class="contact-icon" viewBox="0 0 16 16" aria-hidden="true">
            <circle cx="8" cy="8" r="7" fill="var(--brand-red)"/>
            <path d="M5 8 H11 M8 5 V11" stroke="var(--card)" stroke-width="1.4"/>
          </svg>
          www.vek.example
        </li>
      </ul>
      <p class="service-title">Online Personal Training service</p>
      <p class="tagline">Take control of your personal health<br>to unleash your greatest potential</p>
    </div>
    <div class="brand-panel">
      <span class="brand-dot"></span>
      <span class="brand-wordmark">VEK.PRO</span>
    </div>
  </div>
</body>
</html>
```